Business Cards and Stationary for General Contractor
Kestrel Ductworks, Inc.
I need double sided standard sized Business Card [3.5" x 2"]
Standard Fonts or use use same font as used in logo
Professional
Wesley Ormand
Project Manager
2217 Larkspur Bend, Anchorage, AK 99507
wesley@kdi-northfield.com
www.kdi-northfield.com
Used fonts at recommended. Need Biz Cards, Letterheads, Envelopes.
Use logo. If want to change the way Kestrel Ductworks Incorporated is displayed that's ok or leave as is.
white logo blue background with web address. Other ideas as suggested.

```html
<!DOCTYPE html>
<html lang="en">
<head>
<meta charset="utf-8">
<title>Kestrel Ductworks, Inc. — Stationery Set</title>
<link rel="stylesheet" href="https://fonts.googleapis.com/css2?family=Montserrat:wght@600;700&family=Open+Sans:wght@400;600&display=swap">
<style>
  :root {
    --stage: #d9d9d9;
    --paper: #ffffff;
    --navy: #0d2a6b;
    --blue: #1f56b3;
    --sky: #6f9ad8;
    --rule: #c9d3e6;
    --grid: #b7c0cf;
    --ink: #4a4f5a;
    --label: #6c6c6c;
    --faint: #eef1f6;
  }
  * { box-sizing: border-box; margin: 0; padding: 0; }
  html, body { width: 1200px; height: 343px; overflow: hidden; }
  body {
    background: linear-gradient(#e4e4e4, var(--stage));
    font-family: "Open Sans", Arial, sans-serif;
    color: var(--ink);
    position: relative;
  }
  .piece { position: absolute; background: var(--paper); box-shadow: 0 1px 3px rgba(0,0,0,.25); overflow: hidden; }
  .piece-label {
    position: absolute; top: -9px; left: 0; width: 100%;
    font-size: 4px; color: var(--label); text-align: center; letter-spacing: .2px;
  }
  .sheet { top: 41px; width: 178px; height: 271px; overflow: visible; }
  .sheet-body { position: absolute; inset: 0; overflow: hidden; }
  .brand { position: absolute; display: flex; align-items: center; gap: 3px; }
  .brand-dot { width: 8px; height: 8px; border-radius: 50%; background: var(--blue); flex: none; }
  .brand-name {
    font-family: "Montserrat", Arial, sans-serif; font-weight: 700;
    font-size: 4.6px; color: var(--navy); letter-spacing: .3px; line-height: 1.1;
  }
  .sheet .brand { top: 10px; left: 10px; }
  .contact { position: absolute; font-size: 2.8px; line-height: 1.45; color: var(--ink); }
  .notepad-lines {
    position: absolute; left: 10px; right: 10px; top: 34px; bottom: 14px;
    background: repeating-linear-gradient(to bottom, transparent 0 8.3px, var(--rule) 8.3px 8.8px);
  }
  .ledger-grid {
    position: absolute; left: 8px; right: 8px; top: 30px; bottom: 10px;
    border: .6px solid var(--grid);
    background:
      linear-gradient(to right, transparent 0 24px, var(--grid) 24px 24.6px, transparent 24.6px) 0 0 / 100% 100% no-repeat,
      repeating-linear-gradient(to right, transparent 0 13.3px, var(--grid) 13.3px 13.8px),
      repeating-linear-gradient(to bottom, transparent 0 6.3px, #dde2ea 6.3px 6.7px);
  }
  .fax-table {
    position: absolute; left: 10px; right: 10px; top: 32px;
    border-collapse: collapse; font-size: 3px; color: var(--ink);
  }
  .fax-table td { border: .6px solid var(--grid); height: 7px; padding: 0 2px; }
  .fax-table .field { width: 22px; font-weight: 600; color: var(--navy); }
  .watermark {
    position: absolute; left: 0; right: 0; top: 88px; text-align: center;
    font-family: "Montserrat", Arial, sans-serif; font-weight: 700;
    font-size: 46px; color: var(--faint); letter-spacing: 2px;
  }
  .wave { position: absolute; left: 0; bottom: 0; width: 100%; display: block; }
  .envelope { left: 977px; width: 213px; overflow: visible; }
  .envelope-front { top: 79px; height: 82px; }
  .envelope-back { top: 175px; height: 78px; }
  .envelope .brand { top: 7px; left: 8px; }
  .flap { position: absolute; inset: 0; width: 100%; height: 100%; }
  .card { top: 12px; width: 96px; height: 41px; overflow: visible; }
  .card-front { left: 977px; }
  .card-back { left: 1087px; background: linear-gradient(135deg, var(--blue), var(--navy)); }
  .card-front .brand { top: 5px; left: 5px; }
  .card-person { position: absolute; right: 5px; top: 5px; text-align: right; font-size: 2.8px; line-height: 1.4; }
  .card-person strong { font-family: "Montserrat", Arial, sans-serif; color: var(--navy); font-size: 3.4px; }
  .card-back-name {
    position: absolute; top: 13px; left: 0; width: 100%; text-align: center;
    font-family: "Montserrat", Arial, sans-serif; font-weight: 700; font-size: 6px; color: #fff; letter-spacing: .5px;
  }
  .card-back-web { position: absolute; bottom: 8px; width: 100%; text-align: center; font-size: 3.4px; color: #fff; }
</style>
</head>
<body>

<svg width="0" height="0" style="position:absolute" aria-hidden="true">
  <defs>
    <symbol id="swoosh" viewBox="0 0 180 40" preserveAspectRatio="none">
      <path d="M0 22 C50 6 120 6 180 14 L180 40 L0 40 Z" fill="#6f9ad8"/>
      <path d="M0 28 C55 12 120 12 180 20 L180 40 L0 40 Z" fill="#1f56b3"/>
      <path d="M0 33 C60 20 120 20 180 27 L180 40 L0 40 Z" fill="#0d2a6b"/>
    </symbol>
  </defs>
</svg>

<!-- Notepad -->
<section class="piece sheet" style="left:10px">
  <p class="piece-label">Notepad</p>
  <div class="sheet-body">
    <div class="brand"><span class="brand-dot"></span><span class="brand-name">KESTREL<br>DUCTWORKS, INC.</span></div>
    <div class="notepad-lines"></div>
  </div>
</section>

<!-- Ledger pad -->
<section class="piece sheet" style="left:202px">
  <p class="piece-label">Ledger Pad</p>
  <div class="sheet-body">
    <div class="brand"><span class="brand-dot"></span><span class="brand-name">KESTREL<br>DUCTWORKS, INC.</span></div>
    <p class="contact" style="left:62px;top:10px">2217 Larkspur Bend<br>Anchorage, AK 99507<br>www.kdi-northfield.com</p>
    <div class="ledger-grid"></div>
  </div>
</section>

<!-- Fax form -->
<section class="piece sheet" style="left:396px">
  <p class="piece-label">Fax Form</p>
  <div class="sheet-body">
    <div class="brand"><span class="brand-dot"></span><span class="brand-name">KESTREL<br>DUCTWORKS, INC.</span></div>
    <p class="contact" style="right:10px;top:10px;text-align:right">2217 Larkspur Bend<br>Anchorage, AK 99507<br>www.kdi-northfield.com</p>
    <table class="fax-table">
      <tr><td class="field">To</td><td></td><td class="field">From</td><td></td></tr>
      <tr><td class="field">Date</td><td></td><td class="field">Pages</td><td></td></tr>
      <tr><td class="field">Re</td><td colspan="3"></td></tr>
    </table>
    <div class="watermark" style="top:110px">KDI</div>
    <svg class="wave" height="34"><use href="#swoosh" width="100%" height="34"/></svg>
  </div>
</section>

<!-- Letterhead second page -->
<section class="piece sheet" style="left:590px">
  <p class="piece-label">Letterhead Second</p>
  <div class="sheet-body">
    <div class="brand"><span class="brand-dot"></span><span class="brand-name">KESTREL<br>DUCTWORKS, INC.</span></div>
    <div class="watermark">KDI</div>
    <svg class="wave" height="34"><use href="#swoosh" width="100%" height="34"/></svg>
  </div>
</section>

<!-- Letterhead -->
<section class="piece sheet" style="left:782px">
  <p class="piece-label">Letterhead</p>
  <div class="sheet-body">
    <div class="brand"><span class="brand-dot"></span><span class="brand-name">KESTREL<br>DUCTWORKS, INC.</span></div>
    <p class="contact" style="right:10px;top:10px;text-align:right">2217 Larkspur Bend<br>Anchorage, AK 99507<br>www.kdi-northfield.com</p>
    <div class="watermark">KDI</div>
    <svg class="wave" height="34"><use href="#swoosh" width="100%" height="34"/></svg>
  </div>
</section>

<!-- Business cards -->
<section class="piece card card-front">
  <p class="piece-label">Business Card Front</p>
  <div class="brand"><span class="brand-dot" style="width:6px;height:6px"></span><span class="brand-name" style="font-size:3.4px">KESTREL<br>DUCTWORKS, INC.</span></div>
  <p class="card-person"><strong>Wesley Ormand</strong><br>Project Manager<br>wesley@kdi-northfield.com</p>
  <svg class="wave" height="12"><use href="#swoosh" width="100%" height="12"/></svg>
</section>
<section class="piece card card-back">
  <p class="piece-label">Business Card Back</p>
  <p class="card-back-name">KESTREL DUCTWORKS</p>
  <p class="card-back-web">www.kdi-northfield.com</p>
</section>

<!-- Envelope front -->
<section class="piece envelope envelope-front">
  <p class="piece-label">Envelope Front</p>
  <div class="brand"><span class="brand-dot"></span><span class="brand-name">KESTREL<br>DUCTWORKS, INC.</span></div>
  <p class="contact" style="left:8px;top:20px">2217 Larkspur Bend<br>Anchorage, AK 99507</p>
  <svg class="wave" height="18"><use href="#swoosh" width="100%" height="18"/></svg>
</section>

<!-- Envelope back -->
<section class="piece envelope envelope-back">
  <p class="piece-label">Envelope Back</p>
  <svg class="flap" viewBox="0 0 213 78" preserveAspectRatio="none" aria-hidden="true">
    <path d="M0 0 L106.5 40 L213 0 Z" fill="#1f56b3"/>
    <path d="M0 0 L106.5 34 L213 0 Z" fill="#0d2a6b"/>
    <path d="M0 78 L106.5 44 L213 78" fill="none" stroke="#c9d3e6" stroke-width=".6"/>
  </svg>
  <p class="contact" style="left:0;width:100%;text-align:center;top:48px">www.kdi-northfield.com</p>
</section>

</body>
</html>
```